Designing a Business Card

Hello!

I have started a digital advertising agency, and I'm looking for a design concept for my business card.

The company name is Brindle Metrics. and the info below should appear on the card (feel free to change the layout or structure):

Name: Owen Tarrant
Title: Founder
Address: 412-448 Larkspur Blvd., Winnipeg, MB R2K 4W8, Canada
Office: +1 (833) 555-0172 | +1 (431) 555-0172
Cell: +1 (431) 555-0179
Email: Owen@[login to view URL]
Website: [login to view URL]
Logo: [login to view URL]

The business card size will be 3.5 x 2, double-sided color printing.

I'm looking for a design that will integrate the style of the logo into the entire card theme, so any entry that was made directly from a template will be eliminated from consideration.

```html
<!DOCTYPE html>
<html lang="en">
<head>
<meta charset="utf-8">
<title>Brindle Metrics – Business Card</title>
<link href="https://fonts.googleapis.com/css2?family=Lato:wght@400;700&display=swap" rel="stylesheet">
<style>
  :root {
    --page-bg: #3a3a3c;
    --card-bg: #1f1f21;
    --card-edge: #2a2a2c;
    --text-light: #e8e8e8;
    --text-muted: #8a8a8c;
    --brand-blue: #4a7fd4;
    --brand-red: #e2443a;
    --brand-green: #2fa84f;
    --brand-yellow: #f4c20d;
  }
  * { box-sizing: border-box; margin: 0; padding: 0; }
  html, body {
    width: 1200px; height: 928px; overflow: hidden;
    background: var(--page-bg);
    font-family: "Lato", Arial, sans-serif;
  }
  .card {
    position: absolute;
    width: 700px; height: 400px;
    background: var(--card-bg);
    border: 1px solid var(--card-edge);
    box-shadow: 0 18px 40px rgba(0,0,0,0.45);
    overflow: hidden;
  }
  .card--front { left: 110px; top: 40px; }
  .card--back { left: 390px; top: 488px; }

  .brand-name {
    font-weight: 700;
    color: var(--text-light);
    white-space: nowrap;
  }
  .card--front .brand-name {
    position: absolute; left: 0; right: 0; top: 170px;
    text-align: center; font-size: 52px; letter-spacing: 1px;
  }
  .card--back .brand-name {
    position: absolute; left: 44px; top: 182px;
    font-size: 30px;
  }

  .holder {
    position: absolute; right: 40px; top: 38px; text-align: right;
  }
  .holder__name { font-size: 26px; font-weight: 700; color: var(--brand-blue); }
  .holder__title { font-size: 15px; color: var(--brand-green); margin-top: 2px; }

  .contacts {
    position: absolute; right: 40px; top: 118px;
    list-style: none; text-align: right;
  }
  .contacts__row {
    display: flex; align-items: center; justify-content: flex-end;
    gap: 12px; margin-bottom: 12px;
    font-size: 14px; color: var(--text-light); line-height: 1.35;
  }
  .icon {
    width: 26px; height: 26px; border-radius: 4px;
    display: flex; align-items: center; justify-content: center; flex: none;
  }
  .icon--blue { background: var(--brand-blue); }
  .icon--red { background: var(--brand-red); }
  .icon--green { background: var(--brand-green); }
  .icon--yellow { background: var(--brand-yellow); }
  .icon svg { width: 16px; height: 16px; }

  .address {
    position: absolute; left: 44px; bottom: 42px;
    font-size: 14px; color: var(--text-light); line-height: 1.45;
  }
  .color-strip {
    position: absolute; left: 0; right: 0; bottom: 0; height: 8px; display: flex;
  }
  .color-strip span { flex: 1; }
  .color-strip .blue { background: var(--brand-blue); }
  .color-strip .red { background: var(--brand-red); }
  .color-strip .green { background: var(--brand-green); }
  .color-strip .yellow { background: var(--brand-yellow); }
</style>
</head>
<body>

<section class="card card--front" aria-label="Card front">
  <div class="brand-name">Brindle Metrics</div>
</section>

<section class="card card--back" aria-label="Card back">
  <div class="brand-name">Brindle Metrics</div>

  <div class="holder">
    <div class="holder__name">Owen Tarrant</div>
    <div class="holder__title">Founder</div>
  </div>

  <ul class="contacts">
    <li class="contacts__row">
      <span>+1 (833) 555-0172<br>+1 (431) 555-0172</span>
      <span class="icon icon--blue">
        <svg viewBox="0 0 24 24"><path fill="#1f1f21" d="M6.6 10.8a15.1 15.1 0 0 0 6.6 6.6l2.2-2.2c.3-.3.7-.4 1-.2 1.1.4 2.3.6 3.6.6.6 0 1 .4 1 1V20c0 .6-.4 1-1 1A17 17 0 0 1 3 4c0-.6.4-1 1-1h3.5c.6 0 1 .4 1 1 0 1.3.2 2.5.6 3.6.1.3 0 .7-.2 1z"/></svg>
      </span>
    </li>
    <li class="contacts__row">
      <span>+1 (431) 555-0179</span>
      <span class="icon icon--red">
        <svg viewBox="0 0 24 24"><path fill="#1f1f21" d="M6.6 10.8a15.1 15.1 0 0 0 6.6 6.6l2.2-2.2c.3-.3.7-.4 1-.2 1.1.4 2.3.6 3.6.6.6 0 1 .4 1 1V20c0 .6-.4 1-1 1A17 17 0 0 1 3 4c0-.6.4-1 1-1h3.5c.6 0 1 .4 1 1 0 1.3.2 2.5.6 3.6.1.3 0 .7-.2 1z"/></svg>
      </span>
    </li>
    <li class="contacts__row">
      <span>Owen@brindlemetrics.com</span>
      <span class="icon icon--green">
        <svg viewBox="0 0 24 24"><rect x="3" y="6" width="18" height="12" rx="1" fill="#1f1f21"/><path d="M3.5 6.5 12 13l8.5-6.5" fill="none" stroke="#2fa84f" stroke-width="1.6"/></svg>
      </span>
    </li>
    <li class="contacts__row">
      <span>brindlemetrics.com</span>
      <span class="icon icon--yellow">
        <svg viewBox="0 0 24 24" fill="none" stroke="#1f1f21" stroke-width="1.8"><circle cx="12" cy="12" r="8.5"/><ellipse cx="12" cy="12" rx="3.8" ry="8.5"/><path d="M3.5 12h17M5 7.5h14M5 16.5h14"/></svg>
      </span>
    </li>
  </ul>

  <address class="address" style="font-style:normal">
    412-448 Larkspur Blvd.,<br>
    Winnipeg, MB R2K 4W8, Canada
  </address>

  <div class="color-strip" aria-hidden="true">
    <span class="blue"></span><span class="red"></span><span class="green"></span><span class="yellow"></span>
  </div>
</section>

</body>
</html>
```